Postcard double sided

Title: DWAYNE'S REVENGE

Why would Dwayne Bettancourt align himself with Gerald Ostrander?

(photo of two guys)

Dwayne approached elected officials that he wanted to run for office, but did not have money to finance his campaign. He wanted other elected officials to finance his campaign. Everyone told him that they would help him get the vote out, but that he needed to finance his own race.

In comes Gerald Ostrander.

Gerald Ostrander who has a pay to play scheme over at the City, told Dwayne he would finance his campaign on one condition.

He needed to run against Dennis Varga.

Why would Dwayne want to run with no money?

Backside

DWAYNE'S REVENGE

Dwayne decided to run because no one on the school board would terminate Dwayne's ex and her new boyfriend who both work for the school district. His ex even filed criminal charges against him that are still pending.

Mug Shot facing left (name the charges Criminal Trespass , and Criminal Mischief (highlight bold letters use two lines) mug shot facing right

Complaint one (then photo with full face) Compliant 2)
(showcharges)

Dwayne's ultimate goal is to terminate his ex and her new boyfriend if elected.
Plus Gerald Ostrander needs the majority on the school board to do what he does bet.

Kickbacks for Contracts.

They will hire their own contractors!
Say "No" to Dwayne's Revenge and Gerald Ostrander Money Grab!

Title On Back: all caps: DOMESTIC VIOLENCE

```html
<!DOCTYPE html>
<html lang="en">
<head>
<meta charset="utf-8">
<title>Dwayne's Revenge – Postcard</title>
<link rel="stylesheet" href="https://fonts.googleapis.com/css2?family=Oswald:wght@600;700&family=Francois+One&family=Arimo:wght@400;700&family=Source+Sans+3:wght@400;700&display=swap">
<style>
  :root{
    --page:#d5d5d7;
    --ink:#000000;
    --paper:#ffffff;
    --gold:#f8bd14;
    --red:#e31e25;
    --note:#7a7a7a;
    --photo-a:#5a5550;
    --photo-b:#2b2a2a;
    --mug-a:#8e9094;
    --mug-b:#5e6064;
  }
  *{margin:0;padding:0;box-sizing:border-box}
  html,body{width:1200px;height:2953px;overflow:hidden}
  body{background:var(--page);position:relative;font-family:"Arimo",Arial,sans-serif;color:var(--paper)}

  .card{position:absolute;left:139px;width:954px;height:634px;background:var(--ink);overflow:hidden}
  .card--gold{--accent:var(--gold);--band-ink:var(--ink)}
  .card--red{--accent:var(--red);--band-ink:var(--paper)}

  /* front */
  .front__stripe{position:absolute;left:0;top:0;width:18px;height:537px;background:var(--accent)}
  .front__photo{position:absolute;left:18px;top:0;width:382px;height:537px;
    background:linear-gradient(160deg,var(--photo-a) 0%,var(--photo-b) 70%)}
  .front__title{position:absolute;left:372px;top:24px;width:582px;height:84px;background:var(--accent);
    clip-path:polygon(0 0,100% 0,100% 100%,0 100%,42px 50%);
    display:flex;align-items:center;justify-content:center;padding-left:40px;white-space:nowrap;
    font-family:"Oswald",Impact,sans-serif;font-weight:700;font-size:60px;letter-spacing:1px;color:var(--band-ink);line-height:1}
  .front__copy{position:absolute;left:488px;top:141px;width:450px}
  .lead{font-family:"Arimo",Arial,sans-serif;font-weight:700;color:var(--accent);font-size:21px;line-height:1.2}
  .body{font-size:14px;line-height:1.3;margin-top:10px}
  .lead--mid{margin-top:26px}
  .lead--end{margin-top:24px;white-space:nowrap}
  .band{position:absolute;left:0;bottom:0;width:100%;background:var(--accent);color:var(--band-ink);
    display:flex;align-items:center;justify-content:center;font-family:"Francois One",Impact,sans-serif;white-space:nowrap}
  .front__band{height:97px;font-size:42px}

  /* back */
  .back__title{position:absolute;left:0;top:30px;width:100%;text-align:center;
    font-family:"Oswald",Impact,sans-serif;font-weight:700;font-size:82px;line-height:1;color:var(--accent)}
  .back__intro{position:absolute;left:70px;top:122px;width:814px;text-align:center;font-size:15px;line-height:1.3}
  .mug{position:absolute;top:224px;width:176px;height:180px;background:linear-gradient(180deg,var(--mug-a),var(--mug-b))}
  .mug--left{left:48px}.mug--front{left:235px}.mug--right{left:418px}
  .charge{position:absolute;top:400px;height:40px;background:var(--accent);color:var(--band-ink);
    display:flex;align-items:center;justify-content:center;white-space:nowrap;
    font-family:"Source Sans 3",Arial,sans-serif;font-weight:700;font-size:22px}
  .charge--mischief{left:64px;width:253px;clip-path:polygon(0 0,100% 0,100% 100%,0 100%,16px 50%);padding-left:12px}
  .charge--trespass{left:326px;width:283px;clip-path:polygon(0 0,100% 0,calc(100% - 16px) 50%,100% 100%,0 100%);padding-right:12px}
  .back__goal{position:absolute;left:631px;top:258px;width:260px;font-size:15px;line-height:1.3}
  .kickback__icon{position:absolute;left:213px;top:458px;width:104px;height:74px}
  .kickback__head{position:absolute;left:356px;top:476px;font-family:"Source Sans 3",Arial,sans-serif;font-weight:700;font-size:24px;color:var(--accent)}
  .kickback__text{position:absolute;left:356px;top:510px;font-size:20px}
  .back__band{height:77px;font-size:33px;gap:8px}
  .no-tag{display:inline-block;background:var(--paper);color:var(--red);padding:0 8px;transform:rotate(-10deg);
    font-family:"Francois One",Impact,sans-serif;font-size:30px;line-height:1.25}

  .variant-note{position:absolute;left:0;top:1518px;width:100%;text-align:center;
    font-family:"Source Sans 3",Arial,sans-serif;font-size:21px;color:var(--note);letter-spacing:1px}
</style>
</head>
<body>

<section class="card card--gold front" style="top:95px">
  <div class="front__stripe"></div>
  <div class="front__photo" role="img" aria-label="Photo of two men in suits standing side by side"></div>
  <h1 class="front__title">DWAYNE'S REVENGE</h1>
  <div class="front__copy">
    <p class="lead">Why would Dwayne Bettancourt align himself with Gerald Ostrander?</p>
    <p class="body">Dwayne approached elected officials that he wanted to run for office, but did not have money to finance his campaign. He wanted other elected officials to finance his campaign. Everyone told him that they would help him get the vote out, but that he needed to finance his own race.</p>
    <p class="lead lead--mid">In comes Gerald Ostrander.</p>
    <p class="body">Gerald Ostrander who has a pay to play scheme over at the City, told Dwayne he would finance his campaign on one condition.</p>
    <p class="lead lead--end">He needed to run against Dennis Varga.</p>
  </div>
  <p class="band front__band">Why would Dwayne want to run with no money?</p>
</section>

<section class="card card--gold back" style="top:782px">
  <h2 class="back__title">DOMESTIC VIOLENCE</h2>
  <p class="back__intro">Dwayne decided to run because no one on the school board would terminate Dwayne's ex and her new boyfriend who both work for the school district. His ex even filed criminal charges against him that are still pending.</p>
  <div class="mug mug--left" role="img" aria-label="Mug shot, profile facing left"></div>
  <div class="mug mug--front" role="img" aria-label="Mug shot, profile facing right"></div>
  <div class="mug mug--right" role="img" aria-label="Mug shot, full face"></div>
  <div class="charge charge--mischief">Criminal Mischief</div>
  <div class="charge charge--trespass">Criminal Trespass</div>
  <p class="back__goal">Dwayne's ultimate goal is to terminate his ex and her new boyfriend if elected. Plus Gerald Ostrander needs the majority on the school board to do what he does bet.</p>
  <svg class="kickback__icon" viewBox="0 0 104 74" fill="none" stroke="var(--accent)" stroke-width="3" stroke-linecap="round" stroke-linejoin="round" aria-hidden="true">
    <path d="M14 10 L22 18 L30 10 M22 18 C8 24 6 44 20 46 L28 46 C40 44 38 24 24 18"/>
    <path d="M20 32 h6 M4 52 h14 l16 8 h20 l10 -6 M4 66 h16 l18 4 h22 l14 -10"/>
    <path d="M66 20 l14 -14 l8 8 l-8 18 l6 18 l-10 6 l-14 -20 z"/>
  </svg>
  <p class="kickback__head">Kickbacks for Contracts</p>
  <p class="kickback__text">They will hire their own contractors!</p>
  <p class="band back__band">Say <span class="no-tag">NO!</span> to Dwayne's Revenge and Gerald Ostrander Money Grab!</p>
</section>

<p class="variant-note">IT CAN BE IN ANY COLOR</p>

<section class="card card--red front" style="top:1566px">
  <div class="front__stripe"></div>
  <div class="front__photo" role="img" aria-label="Photo of two men in suits standing side by side"></div>
  <h1 class="front__title">DWAYNE'S REVENGE</h1>
  <div class="front__copy">
    <p class="lead">Why would Dwayne Bettancourt align himself with Gerald Ostrander?</p>
    <p class="body">Dwayne approached elected officials that he wanted to run for office, but did not have money to finance his campaign. He wanted other elected officials to finance his campaign. Everyone told him that they would help him get the vote out, but that he needed to finance his own race.</p>
    <p class="lead lead--mid">In comes Gerald Ostrander.</p>
    <p class="body">Gerald Ostrander who has a pay to play scheme over at the City, told Dwayne he would finance his campaign on one condition.</p>
    <p class="lead lead--end">He needed to run against Dennis Varga.</p>
  </div>
  <p class="band front__band">Why would Dwayne want to run with no money?</p>
</section>

<section class="card card--red back" style="top:2253px">
  <h2 class="back__title">DOMESTIC VIOLENCE</h2>
  <p class="back__intro">Dwayne decided to run because no one on the school board would terminate Dwayne's ex and her new boyfriend who both work for the school district. His ex even filed criminal charges against him that are still pending.</p>
  <div class="mug mug--left" role="img" aria-label="Mug shot, profile facing left"></div>
  <div class="mug mug--front" role="img" aria-label="Mug shot, profile facing right"></div>
  <div class="mug mug--right" role="img" aria-label="Mug shot, full face"></div>
  <div class="charge charge--mischief">Criminal Mischief</div>
  <div class="charge charge--trespass">Criminal Trespass</div>
  <p class="back__goal">Dwayne's ultimate goal is to terminate his ex and her new boyfriend if elected. Plus Gerald Ostrander needs the majority on the school board to do what he does bet.</p>
  <svg class="kickback__icon" viewBox="0 0 104 74" fill="none" stroke="var(--paper)" stroke-width="3" stroke-linecap="round" stroke-linejoin="round" aria-hidden="true">
    <path d="M14 10 L22 18 L30 10 M22 18 C8 24 6 44 20 46 L28 46 C40 44 38 24 24 18"/>
    <path d="M20 32 h6 M4 52 h14 l16 8 h20 l10 -6 M4 66 h16 l18 4 h22 l14 -10"/>
    <path d="M66 20 l14 -14 l8 8 l-8 18 l6 18 l-10 6 l-14 -20 z"/>
  </svg>
  <p class="kickback__head">Kickbacks for Contracts</p>
  <p class="kickback__text">They will hire their own contractors!</p>
  <p class="band back__band">Say <span class="no-tag">NO!</span> to Dwayne's Revenge and Gerald Ostrander Money Grab!</p>
</section>

</body>
</html>
```